Visitenkarten für Erstellung von Beleihungswert- und Verkehrswertgutachten.
Zielgruppe
Ich erstelle Beleihungswert- und Verkehrswertgutachten.
Meine Zielgruppe sind alle Immobilieneigentümer, Kaufinteressenten, Erben von Immobilienvermögen evtl. auch Anwälte, Steuerberater.
Aufgabenstellung
Der Fokus liegt auf der Wertermittlung von Immobilien

```html
<!DOCTYPE html>
<html lang="de">
<head>
<meta charset="utf-8">
<title>Visitenkarten – Korvath Immobilien Bewertung</title>
<link href="https://fonts.googleapis.com/css2?family=Exo+2:wght@400;500&display=swap" rel="stylesheet">
<style>
  :root {
    --navy: #1b1846;
    --magenta: #e0137a;
    --paper: #ffffff;
    --ink: #3a3a44;
    --stage: #ffffff;
    --shadow: rgba(40, 36, 90, 0.22);
  }
  * { box-sizing: border-box; margin: 0; padding: 0; }
  html, body {
    width: 1200px; height: 1194px; overflow: hidden;
    background: var(--stage);
    font-family: "Exo 2", "Helvetica Neue", Arial, sans-serif;
  }
  .sheet { position: relative; width: 1200px; height: 1194px; }

  .card {
    position: absolute; width: 466px; height: 302px;
    background: var(--paper);
    box-shadow: 14px 16px 22px var(--shadow);
    overflow: hidden;
  }
  .card--front { left: 96px; top: 235px; background: var(--navy); }
  .card--back-narrow { left: 614px; top: 235px; }
  .card--back-wide { left: 96px; top: 584px; height: 300px; }

  /* front */
  .brand {
    position: absolute; left: 0; right: 0; top: 136px;
    display: flex; align-items: center; justify-content: center; gap: 12px;
    color: var(--paper);
  }
  .brand__mark { width: 16px; height: 16px; background: var(--magenta); flex: none; }
  .brand__name { font-size: 24px; font-weight: 500; line-height: 1; white-space: nowrap; }

  /* back */
  .back__header {
    position: absolute; left: 0; top: 0; width: 100%; height: 141px;
    background: var(--navy); border-bottom: 5px solid var(--magenta);
    color: var(--paper);
  }
  .person { position: absolute; top: 56px; }
  .person__name { font-size: 21px; font-weight: 500; line-height: 1; white-space: nowrap; }
  .person__role { margin-top: 8px; margin-left: 2px; font-size: 13px; }
  .divider { position: absolute; top: 57px; width: 5px; height: 45px; background: var(--magenta); }
  .contact { position: absolute; top: 53px; font-size: 15px; line-height: 17px; font-style: normal; white-space: nowrap; }
  .credentials {
    position: absolute; font-size: 10.5px; line-height: 16.5px; color: var(--ink); white-space: nowrap;
  }

  .card--back-narrow .person { left: 38px; }
  .card--back-narrow .divider { left: 178px; }
  .card--back-narrow .contact { left: 201px; }
  .card--back-narrow .credentials { left: 203px; top: 160px; }

  .card--back-wide .person { left: 47px; top: 59px; }
  .card--back-wide .divider { left: 187px; }
  .card--back-wide .contact { left: 210px; }
  .card--back-wide .credentials { left: 48px; top: 193px; }
</style>
</head>
<body>
<main class="sheet">

  <section class="card card--front">
    <div class="brand">
      <span class="brand__mark"></span>
      <span class="brand__name">Korvath Immobilien Bewertung</span>
    </div>
  </section>

  <section class="card card--back-narrow">
    <header class="back__header">
      <div class="person">
        <div class="person__name">Lena Korvath</div>
        <div class="person__role">Geschäftsführer</div>
      </div>
      <span class="divider"></span>
      <address class="contact">
        Lindenhof-Weg 4/2<br>70599 Musterstadt<br>Mobil: 0171 5550123
      </address>
    </header>
    <p class="credentials">
      DIN ISO/IEC 17024 zertifizierte Bau-<br>
      Sachverständige für die Markt-<br>
      und Beleihungswertermittlung von<br>
      Wohn- und Gewerbeimmobilie<br>
      VERIQ D1,03 und D3 zertifiziert<br>
      SIGEKO = Sicherheits- und<br>
      Gesundheitsschutz-Koordinator für Baustellen.
    </p>
  </section>

  <section class="card card--back-wide">
    <header class="back__header">
      <div class="person">
        <div class="person__name">Lena Korvath</div>
        <div class="person__role">Geschäftsführer</div>
      </div>
      <span class="divider"></span>
      <address class="contact">
        Lindenhof-Weg 4/2<br>70599 Musterstadt<br>Mobil: 0171 5550123
      </address>
    </header>
    <p class="credentials">
      DIN ISO/IEC 17024 zertifizierte Bau-Sachverständige für die Markt-<br>
      und Beleihungswertermittlung von Wohn- und Gewerbeimmobilie<br>
      VERIQ D1,03 und D3 zertifiziert<br>
      SIGEKO = Sicherheits- und Gesundheitsschutz-Koordinator für Baustellen.
    </p>
  </section>

</main>
</body>
</html>
```